Cell phone repair

you can please design me business card

size 3.5" x 2"

colors blue and red

fixit rapid logo (you get from my website fixitrapidco.example )

"We Come To You!

It is very simple! You tell us what phone you have, And we come to fix it."

phone number: 555.248.3906

website: www.fixitrapidco.example

email: info@fixitrapidco.example

```html
<!DOCTYPE html>
<html lang="en">
<head>
<meta charset="UTF-8">
<title>Fixit Rapid – Business Card</title>
<link href="https://fonts.googleapis.com/css2?family=Open+Sans:wght@400;600&display=swap" rel="stylesheet">
<style>
  :root {
    --brand-blue: #1f9fe0;
    --brand-red: #e5202e;
    --ink: #2b2b2b;
    --card: #ffffff;
    --backdrop: #eceaeb;
    --phone-light: #2f6fc4;
    --phone-dark: #0f2a55;
  }
  * { box-sizing: border-box; margin: 0; padding: 0; }
  html, body { width: 1200px; height: 1200px; overflow: hidden; }
  body {
    background: var(--backdrop);
    font-family: "Open Sans", Arial, sans-serif;
    color: var(--ink);
    position: relative;
  }
  .card {
    position: absolute;
    left: 180px;
    width: 840px;
    height: 480px;
    background: var(--card);
    border-radius: 36px;
    overflow: hidden;
    box-shadow: 0 12px 30px rgba(0,0,0,0.18);
  }
  .card--front { top: 90px; }
  .card--back { top: 630px; }

  .brand {
    display: flex;
    align-items: center;
    gap: 14px;
    position: absolute;
  }
  .brand__name {
    font-weight: 600;
    font-size: 40px;
    color: var(--brand-blue);
    letter-spacing: 0.5px;
  }
  .brand__dot {
    width: 44px; height: 44px;
    border-radius: 50%;
    background: var(--brand-red);
  }
  .card--front .brand { left: 50%; top: 46px; transform: translateX(-50%); }

  .device-swap {
    position: absolute;
    left: 50%; top: 130px;
    transform: translateX(-50%);
    display: flex; align-items: center; gap: 40px;
  }
  .device-photo {
    width: 96px; height: 150px;
    border-radius: 12px;
    background: linear-gradient(150deg, var(--phone-light), var(--phone-dark));
  }
  .device-photo--back { background: linear-gradient(160deg, #28487e, var(--phone-dark)); }

  .divider {
    position: absolute;
    left: 80px; right: 80px; top: 318px;
    height: 2px; background: var(--brand-blue);
  }
  .tagline {
    position: absolute;
    left: 0; right: 0; top: 340px;
    text-align: center;
    font-size: 22px;
    line-height: 1.6;
  }

  .card--back .brand { left: 110px; top: 200px; }
  .contact-rule {
    position: absolute;
    left: 470px; top: 90px;
    width: 2px; height: 250px;
    background: var(--brand-blue);
    opacity: 0.6;
  }
  .contact {
    position: absolute;
    left: 505px; top: 96px;
  }
  .contact__name { font-size: 30px; font-weight: 400; letter-spacing: 1px; }
  .contact__name .first { color: var(--brand-blue); }
  .contact__name .last { color: var(--brand-red); }
  .contact__role { font-size: 19px; margin-bottom: 28px; }
  .contact__list { list-style: none; font-size: 18px; line-height: 1.9; }
  .contact__list li { display: flex; align-items: center; gap: 12px; }
  .contact__list svg { width: 20px; height: 20px; fill: var(--brand-red); flex: none; }
  .band {
    position: absolute;
    left: 0; right: 0; bottom: 0;
    height: 34px;
    background: var(--brand-blue);
  }
</style>
</head>
<body>

<section class="card card--front">
  <div class="brand">
    <span class="brand__name">Fixit Rapid</span>
    <span class="brand__dot"></span>
  </div>

  <div class="device-swap">
    <div class="device-photo" role="img" aria-label="Photo of a smartphone front screen"></div>
    <svg width="64" height="30" viewBox="0 0 64 30" aria-hidden="true">
      <rect x="0" y="11" width="44" height="8" fill="#e5202e"/>
      <polygon points="42,0 64,15 42,30" fill="#e5202e"/>
    </svg>
    <div class="device-photo device-photo--back" role="img" aria-label="Photo of a repaired smartphone back"></div>
  </div>

  <div class="divider"></div>

  <p class="tagline">"We Come To You! It is very simple!<br>You tell us what phone you have, And we come to fix it."</p>
</section>

<section class="card card--back">
  <div class="brand">
    <span class="brand__name">Fixit Rapid</span>
    <span class="brand__dot"></span>
  </div>

  <div class="contact-rule"></div>

  <div class="contact">
    <h1 class="contact__name"><span class="first">SAM</span> <span class="last">RIVERA</span></h1>
    <p class="contact__role">Director</p>
    <ul class="contact__list">
      <li>
        <svg viewBox="0 0 24 24" aria-hidden="true"><path d="M6.6 10.8a15.1 15.1 0 0 0 6.6 6.6l2.2-2.2a1 1 0 0 1 1-.25 11.4 11.4 0 0 0 3.6.57 1 1 0 0 1 1 1V20a1 1 0 0 1-1 1A17 17 0 0 1 3 4a1 1 0 0 1 1-1h3.5a1 1 0 0 1 1 1 11.4 11.4 0 0 0 .57 3.6 1 1 0 0 1-.25 1z"/></svg>
        555.248.3906
      </li>
      <li>
        <svg viewBox="0 0 24 24" aria-hidden="true"><path d="M12 2a10 10 0 1 0 0 20 10 10 0 0 0 0-20zm6.9 6h-2.9a15.7 15.7 0 0 0-1.4-3.6A8 8 0 0 1 18.9 8zM12 4a14 14 0 0 1 1.9 4h-3.8A14 14 0 0 1 12 4zM4.3 14a8 8 0 0 1 0-4h3.4a16 16 0 0 0 0 4zm.8 2h2.9a15.7 15.7 0 0 0 1.4 3.6A8 8 0 0 1 5.1 16zM8 8H5.1a8 8 0 0 1 4.3-3.6A15.7 15.7 0 0 0 8 8zm4 12a14 14 0 0 1-1.9-4h3.8A14 14 0 0 1 12 20zm2.3-6H9.7a14.7 14.7 0 0 1 0-4h4.6a14.7 14.7 0 0 1 0 4zm.3 5.6a15.7 15.7 0 0 0 1.4-3.6h2.9a8 8 0 0 1-4.3 3.6zM16.3 14a16 16 0 0 0 0-4h3.4a8 8 0 0 1 0 4z"/></svg>
        www.fixitrapidco.example
      </li>
      <li>
        <svg viewBox="0 0 24 24" aria-hidden="true"><path d="M2 5h20v14H2zm2 2v.4l8 5.2 8-5.2V7zm0 2.8V17h16V9.8l-8 5.2z"/></svg>
        info@fixitrapidco.example
      </li>
    </ul>
  </div>

  <div class="band"></div>
</section>

</body>
</html>
```